Non Profit Company Looking For New Website

The website for Corvale Paddock Rehoming Society should offer the viewer beautiful photos that inspire condifence and joy and tap into our love of horses.

We would like to see a website that displays trust, quality and confidence. Needs to be responsive and mobile friendly for all browsers and coded for both Android & IOS.

READ ATTACHED WEBSITE TEMPLATE FOR COMPLETE DETAILS ON WHAT WE ARE LOOKING FOR.

Looking for recommmendations if we should use WordPress/WooCommerce for site or Wordpress with Shopify Plug in or just Shopify.

Must be both desktop and mobile friendly with fast page load speed. Need the ability to edit ourselves.

Industry/Entity Type

Non Profit

Coding

Coded - Design and coding required

Number of Pages Required

5+ page

Requirements
Must have
• We would like to see a website that displays trust, quality and confidence. Needs to be responsive and mobile friendly for all browsers and coded for both Android & IOS.

Looking for recommendations if we should use WordPress/WooCommerce for site or Wordpress with Shopify Plug in or just Shopify.

Logo Colour:
Pantone 7621 C

READ TEMPLATE THAT IS ATTACHED
Nice to have
• Like look of this website as a sample:
https://www.quillmanegallop.com/

Another similar non profit organization
https://brindlefieldrest.com/

```html
<!DOCTYPE html>
<html lang="en">
<head>
<meta charset="utf-8">
<title>Corvale Paddock Rehoming Society</title>
<link href="https://fonts.googleapis.com/css2?family=Playfair+Display:wght@400;500;600&family=Lora:wght@400;600;700&display=swap" rel="stylesheet">
<style>
:root{
  --brand-red:#a6192e;
  --green:#1fb54a;
  --ink:#1c1c1c;
  --body:#3b3b3b;
  --link:#3a4f8c;
  --grey-band:#f1f1f1;
  --line:#d9d9d9;
  --white:#ffffff;
  --teal:#20b59a;
}
*{box-sizing:border-box;margin:0;padding:0}
html,body{width:1200px;height:4011px;overflow:hidden}
body{position:relative;font-family:"Lora",Georgia,serif;color:var(--body);background:var(--white)}
.abs{position:absolute}
.serif-display{font-family:"Playfair Display",Georgia,serif;color:var(--ink);font-weight:500}
.center{text-align:center}

/* header */
.site-header{position:absolute;top:0;left:0;width:1200px;height:81px;background:var(--white)}
.brand{position:absolute;left:48px;top:14px;width:110px;text-align:center;color:var(--brand-red);font-family:"Lora",serif;font-size:11px;font-weight:600;line-height:1.3;letter-spacing:.5px;text-transform:uppercase}
.main-nav{position:absolute;right:48px;top:27px;display:flex;gap:26px;align-items:center;font-size:9.5px;font-weight:600;letter-spacing:.6px}
.main-nav a{color:#4a4a4a;text-decoration:none}
.main-nav a.active{color:var(--brand-red)}
.main-nav a.pill{border:1.5px solid #555;border-radius:16px;padding:7px 10px}

/* hero */
.hero{position:absolute;top:81px;left:0;width:1200px;height:462px;background:linear-gradient(180deg,#2f4a26 0%,#3d6a2c 45%,#2e6b25 75%,#2d5d21 100%)}
.hero h1{position:absolute;top:112px;left:200px;width:800px;font-size:42px;line-height:1.05;color:var(--white);font-weight:600}
.btn{position:absolute;display:flex;align-items:center;justify-content:center;border-radius:22px;font-size:10.5px;font-weight:700;letter-spacing:.3px;text-transform:uppercase;text-decoration:none}
.btn-solid{background:var(--green);color:var(--white)}
.btn-outline{border:1.5px solid var(--green);color:var(--green)}

/* intro */
.intro{position:absolute;top:543px;left:0;width:1200px;height:598px;background:var(--grey-band)}
.intro h2{position:absolute;top:56px;left:0;width:1200px;font-size:44px;line-height:1.1}
.intro p{position:absolute;top:170px;left:400px;width:400px;font-size:12px;line-height:1.7}
.intro .photo{position:absolute;top:243px;left:222px;width:751px;height:355px;background:radial-gradient(ellipse at 55% 70%,#bdbdbd 0%,#e6e6e6 45%,#f1f1f1 80%)}

/* about */
.about h2{position:absolute;top:1196px;left:0;width:1200px;font-size:33px;line-height:1.1}
.about p{position:absolute;left:400px;width:400px;font-size:12px;line-height:1.7;text-align:center}

/* adopt */
.adopt-photo{position:absolute;top:1614px;left:600px;width:600px;height:659px;background:radial-gradient(ellipse at 75% 20%,#f6d24a 0%,#d99a1c 40%,#8a5a12 75%,#5a3a0e 100%)}
.adopt h2{position:absolute;top:1868px;left:0;width:600px;font-size:32px}
.adopt p{position:absolute;top:1922px;left:100px;width:400px;font-size:11px;line-height:1.6;color:var(--link);text-align:center}

/* horses */
.horses h2{position:absolute;top:2322px;left:0;width:1200px;font-size:42px}
.horse-card{position:absolute;top:2424px;width:114px;text-align:center;font-size:11px;font-weight:600;color:var(--ink)}
.horse-card .thumb{height:125px;background:linear-gradient(180deg,#9fc3e6 0%,#7fa35c 55%,#6b5a3a 100%)}
.horse-card .name{margin-top:12px;font-family:"Playfair Display",serif;font-weight:500;font-size:13px;color:#555}
.horse-card .tag{display:inline-block;margin-top:6px;background:var(--teal);color:var(--white);font-size:5.5px;padding:2px 5px;letter-spacing:.3px}
.horse-card .fee{margin-top:10px;font-size:12px;line-height:1.45}
.horse-card .row{font-size:10px}
.horse-card .more{display:inline-block;color:var(--link);font-weight:400;font-size:9.5px;border-bottom:1px solid var(--link);padding:0 6px 2px}

/* contact */
.contact{position:absolute;top:3011px;left:0;width:1200px;height:720px;background:var(--grey-band)}
.contact h2{position:absolute;top:62px;left:0;width:1200px;font-size:33px;line-height:1.1}
.contact .lede{position:absolute;top:148px;left:0;width:1200px;font-size:11px;text-align:center}
.info-block{position:absolute;font-size:11px;line-height:1.8;color:#4a4a4a}
.info-block h3{font-family:"Lora",serif;font-size:15px;font-weight:600;color:var(--ink);margin:18px 0 2px}
.field-label{position:absolute;left:625px;font-size:10.5px;font-weight:700;color:var(--ink)}
.field-label span{color:var(--brand-red)}
.field{position:absolute;left:625px;width:347px;background:var(--white);border:1px solid var(--line);border-radius:8px}
.submit{position:absolute;left:709px;top:597px;width:178px;height:31px;border:1.5px solid var(--brand-red);border-radius:8px;color:var(--brand-red);font-size:11px;font-weight:600;display:flex;align-items:center;justify-content:center;background:var(--white)}

/* footer */
.site-footer{position:absolute;top:3750px;left:0;width:1200px;height:261px;background:#f7f7f7}
.footer-org{position:absolute;left:224px;top:48px;width:160px;font-size:9.5px;line-height:1.6;color:#4a4a4a}
.footer-org strong{display:block;color:var(--ink);margin-bottom:14px}
.footer-links{position:absolute;left:418px;top:48px;font-size:9.5px;line-height:2.2;color:#4a4a4a}
.footer-links .pill{border:1.2px solid #555;border-radius:12px;padding:2px 8px}
.copyright{position:absolute;left:224px;top:214px;font-size:9.5px;color:#4a4a4a}
.copyright .muted{color:var(--brand-red)}
.social{position:absolute;left:896px;top:212px;display:flex;gap:18px}
.social span{width:11px;height:11px;border-radius:50%;background:#222;display:block}
</style>
</head>
<body>

<header class="site-header">
  <div class="brand">Corvale Paddock<br>Rehoming Society</div>
  <nav class="main-nav">
    <a class="active" href="#">HOME</a>
    <a href="#">ABOUT</a>
    <a href="#">ADOPT</a>
    <a href="#">HORSES</a>
    <a class="pill" href="#">DONATE &amp; SHOP</a>
    <a href="#">CONTACT US</a>
  </nav>
</header>

<section class="hero" role="img" aria-label="A horse grazing in a green paddock beside white fencing and willow trees">
  <h1 class="serif-display center">We support and develop retired thoroughbred racehorses for their next chapter in life</h1>
  <a class="btn btn-outline" href="#" style="left:450px;top:304px;width:190px;height:36px">Adopt a Thoroughbred</a>
  <a class="btn btn-solid" href="#" style="left:646px;top:304px;width:104px;height:36px">Donate Us</a>
</section>

<section class="intro">
  <h2 class="serif-display center">Retire. Retrain.<br>Rehome.</h2>
  <p class="center"><strong style="color:var(--ink)">Corvale Paddock Rehoming Society</strong> (CPRS) is a registered not-for-profit organization in Westmark.</p>
  <div class="photo" role="img" aria-label="Soft black and white portrait of a grey horse's head"></div>
</section>

<section class="about">
  <h2 class="serif-display center">What is Thoroughbred<br>Aftercare?</h2>
  <p style="top:1312px"><strong style="color:var(--ink)">The health</strong>, <strong style="color:var(--ink)">safety</strong> and <strong style="color:var(--ink)">welfare</strong> of our equine athletes does not end at the finish line, and retirement and aftercare are critical to the success of the racing industry.</p>
  <p style="top:1390px">Aftercare is the safe placement of racehorses after their careers as racehorse are completed. Some horses might retire to the breeding shed or broodmare bands, while others are retrained for second careers.</p>
  <a class="btn btn-solid" href="#" style="left:513px;top:1515px;width:174px;height:37px">Learn More About Us</a>
</section>

<section class="adopt">
  <h2 class="serif-display center">Adopt a Horse</h2>
  <p>Corvale Paddock Rehoming is committed to helping match you with the perfect horse.</p>
  <a class="btn btn-solid" href="#" style="left:245px;top:1977px;width:110px;height:36px">Adopt Now</a>
  <div class="adopt-photo" role="img" aria-label="A rider greeting a bay horse in a sunlit meadow"></div>
</section>

<section class="horses">
  <h2 class="serif-display center">Our Horses</h2>

  <article class="horse-card" style="left:409px">
    <div class="thumb" role="img" aria-label="Bay horse standing in a field"></div>
    <div class="name">Marrow Bay</div>
    <div class="tag">OUR HORSES</div>
    <div class="fee">FEE $1,000—NOW<br>$800 UNTIL 5/31</div>
    <div class="row" style="margin-top:14px">Height 15.3</div>
    <div class="row" style="margin-top:20px">Birth Year 2016</div>
    <div class="row" style="margin-top:12px;line-height:1.6">Color Bay<br>Gender Gelding</div>
    <div class="row" style="margin-top:19px">Location</div>
    <div class="row" style="margin-top:42px">FERNDALE BEND, WM</div>
    <div style="margin-top:26px"><span class="more">Read More</span></div>
  </article>

  <article class="horse-card" style="left:543px">
    <div class="thumb" role="img" aria-label="Chestnut horse standing in a sand paddock"></div>
    <div class="name">Tallow Run</div>
    <div class="tag">OUR HORSES</div>
    <div class="fee">FEE $1,000—NOW<br>$800 UNTIL 5/31</div>
    <div class="row" style="margin-top:14px">Height 15.3</div>
    <div class="row" style="margin-top:20px">Birth Year 2016</div>
    <div class="row" style="margin-top:12px;line-height:1.6">Color Bay<br>Gender Gelding</div>
    <div class="row" style="margin-top:19px">Location</div>
    <div class="row" style="margin-top:42px">FERNDALE BEND, WM</div>
    <div style="margin-top:26px"><span class="more">Read More</span></div>
  </article>

  <article class="horse-card" style="left:677px">
    <div class="thumb" role="img" aria-label="Dark bay horse in a grassy field"></div>
    <div class="name">Quiet Lantern</div>
    <div class="tag">OUR HORSES</div>
    <div class="fee">FEE $1,000—NOW<br>$800 UNTIL 5/31</div>
    <div class="row" style="margin-top:14px">Height 15.3</div>
    <div class="row" style="margin-top:20px">Birth Year 2016</div>
    <div class="row" style="margin-top:12px;line-height:1.6">Color Bay<br>Gender Gelding</div>
    <div class="row" style="margin-top:19px">Location</div>
    <div class="row" style="margin-top:42px">FERNDALE BEND, WM</div>
    <div style="margin-top:26px"><span class="more">Read More</span></div>
  </article>

  <a class="btn btn-solid" href="#" style="left:521px;top:2931px;width:158px;height:37px">More Ways to Give</a>
</section>

<section class="contact">
  <h2 class="serif-display center">Have a question or need<br>more information?</h2>
  <div class="lede">Give us a call or use the form below.</div>

  <div class="info-block" style="left:224px;top:236px">
    <svg width="18" height="18" viewBox="0 0 18 18"><circle cx="9" cy="9" r="9" fill="var(--brand-red)"/><path d="M9 4.2a3 3 0 0 0-3 3c0 2.2 3 5.8 3 5.8s3-3.6 3-5.8a3 3 0 0 0-3-3z" fill="#fff"/><circle cx="9" cy="7.2" r="1.1" fill="var(--brand-red)"/></svg>
    <h3>Location</h3>
    42 Hollin Ridge Road<br>Ferndale Bend<br>Westmark<br>T0L 2B4
  </div>

  <div class="info-block" style="left:423px;top:236px">
    <svg width="18" height="18" viewBox="0 0 18 18"><circle cx="9" cy="9" r="9" fill="var(--brand-red)"/><path d="M9 4.2a3 3 0 0 0-3 3c0 2.2 3 5.8 3 5.8s3-3.6 3-5.8a3 3 0 0 0-3-3z" fill="#fff"/><circle cx="9" cy="7.2" r="1.1" fill="var(--brand-red)"/></svg>
    <h3>Call Us</h3>
    +1 555 0148 220
  </div>

  <div class="info-block" style="left:423px;top:330px">
    <svg width="18" height="18" viewBox="0 0 18 18"><circle cx="9" cy="9" r="9" fill="var(--brand-red)"/><path d="M9 4.2a3 3 0 0 0-3 3c0 2.2 3 5.8 3 5.8s3-3.6 3-5.8a3 3 0 0 0-3-3z" fill="#fff"/><circle cx="9" cy="7.2" r="1.1" fill="var(--brand-red)"/></svg>
    <h3>E-Mail</h3>
    hello@corvalepaddock.org
  </div>

  <div class="field-label" style="top:222px">Name <span>*</span></div>
  <div class="field" style="top:241px;height:28px"></div>
  <div class="field-label" style="top:293px">Email <span>*</span></div>
  <div class="field" style="top:311px;height:28px"></div>
  <div class="field-label" style="top:364px">Phone</div>
  <div class="field" style="top:381px;height:28px"></div>
  <div class="field-label" style="top:435px">Message <span>*</span></div>
  <div class="field" style="top:451px;height:123px"></div>
  <div class="submit">Submit</div>
</section>

<footer class="site-footer">
  <div class="footer-org">
    <strong>Corvale Paddock Rehoming Society</strong>
    42 Hollin Ridge Road<br>Ferndale Bend<br>Westmark<br>T0L 2B4<br>555-0192-447
  </div>
  <div class="footer-links">
    Home<br>About<br>Adopt<br>Horses<br><span class="pill">Donate &amp; Shop</span><br>Contact Us
  </div>
  <div class="copyright">Copyright © 2021. 0.0.0b. - Dev version - <span class="muted">Dana Whitlow</span></div>
  <div class="social"><span></span><span></span><span></span></div>
</footer>

</body>
</html>
```